LPS AUDITION

I need a post card design (front only) with this on it:
Leap Pulse Stride (this is the main title to be in all caps)
Auditions
Date: Thursday June 30th
6:30-8:30 PM in person
Address: 4172 Kestrel BLVD, Oakland CA 94605
video submissions turn in by Sunday July 3rd, 2022 email:LeapPulseStride22@movenote.test
Teens and Adults welcomed

SO PLEASE COME UP WITH A DESIGN THATS COLORFUL AND INVITING THX!

```html
<!DOCTYPE html>
<html lang="en">
<head>
<meta charset="utf-8">
<title>Leap Pulse Stride Auditions Postcard</title>
<link href="https://fonts.googleapis.com/css2?family=Oswald:wght@600;700&family=Italianno&family=Pinyon+Script&family=Open+Sans:wght@400;600;700&display=swap" rel="stylesheet">
<style>
  :root {
    --plum-deep: #1d0b24;
    --plum: #3b1846;
    --violet: #6a3a86;
    --magenta: #e5147a;
    --magenta-dark: #a80d5a;
    --white: #ffffff;
  }
  * { margin: 0; padding: 0; box-sizing: border-box; }
  html, body { width: 1200px; height: 842px; overflow: hidden; background: #ffffff; }
  .postcard {
    position: relative;
    width: 1200px;
    height: 842px;
    overflow: hidden;
    background:
      radial-gradient(ellipse 420px 300px at 540px 400px, rgba(30,8,40,0.9), transparent 70%),
      radial-gradient(ellipse 380px 420px at 1080px 260px, rgba(200,170,200,0.5), transparent 70%),
      radial-gradient(ellipse 300px 260px at 90px 170px, rgba(190,140,170,0.4), transparent 70%),
      linear-gradient(135deg, var(--plum) 0%, var(--violet) 35%, var(--plum-deep) 60%, var(--violet) 100%);
  }
  .backdrop-texture { position: absolute; inset: 0; }
  .frame {
    position: absolute;
    left: 20px; top: 21px; right: 20px; bottom: 23px;
    border: 2px solid var(--magenta);
  }
  .title {
    position: absolute;
    left: 0; width: 1180px; top: 74px;
    text-align: center;
    font-family: "Oswald", sans-serif;
    font-weight: 700;
    font-size: 122px;
    line-height: 1;
    letter-spacing: 2px;
    color: var(--white);
    text-shadow: 3px 3px 0 var(--magenta), -1px -1px 0 var(--magenta), 1px -1px 0 var(--magenta), -1px 1px 0 var(--magenta);
  }
  .subtitle {
    position: absolute;
    left: 0; width: 1180px; top: 206px;
    text-align: center;
    font-family: "Italianno", cursive;
    font-size: 176px;
    line-height: 1;
    color: var(--magenta);
  }
  .date-ribbon { position: absolute; left: 138px; top: 352px; width: 836px; height: 54px; }
  .date-text {
    position: absolute;
    left: 150px; width: 812px; top: 355px; height: 48px;
    display: flex; align-items: center; justify-content: center;
    font-family: "Oswald", sans-serif;
    font-weight: 600;
    font-size: 34px;
    letter-spacing: 0.5px;
    color: var(--white);
  }
  .address {
    position: absolute;
    left: 0; width: 1180px; top: 428px;
    text-align: center;
    font-family: "Open Sans", sans-serif;
    font-weight: 600;
    font-size: 33px;
    color: var(--white);
  }
  .welcome {
    position: absolute;
    left: 0; width: 1160px; top: 508px;
    text-align: center;
    font-family: "Pinyon Script", cursive;
    font-size: 46px;
    color: var(--white);
  }
  .dancer-art {
    position: absolute;
    left: 830px; top: 480px; width: 280px; height: 318px;
    border-radius: 45% 45% 40% 40%;
    background:
      radial-gradient(ellipse 80px 130px at 50% 45%, rgba(70,20,70,0.95), transparent 75%),
      radial-gradient(ellipse 140px 150px at 55% 60%, rgba(242,194,48,0.75), transparent 75%);
  }
  .details {
    position: absolute;
    left: 84px; top: 716px;
    font-family: "Open Sans", sans-serif;
    font-size: 25px;
    color: var(--white);
    list-style: none;
  }
  .details li { display: flex; align-items: center; height: 38px; }
  .details strong { font-weight: 700; margin-left: 0.3em; }
  .details .marker { width: 26px; height: 26px; margin-right: 10px; flex: none; }
</style>
</head>
<body>
<main class="postcard">
  <svg class="backdrop-texture" width="1200" height="842" viewBox="0 0 1200 842" aria-hidden="true">
    <defs>
      <linearGradient id="panel-shade" x1="0" y1="0" x2="1" y2="0">
        <stop offset="0" stop-color="#0f0f0f"/>
        <stop offset="0.55" stop-color="#3a3a3a"/>
        <stop offset="1" stop-color="#1a1a1a"/>
      </linearGradient>
    </defs>
    <path d="M0 645 C 300 705, 600 720, 850 665 C 1000 630, 1100 590, 1200 555 L1200 842 L0 842 Z" fill="url(#panel-shade)"/>
    <path d="M0 640 C 300 700, 600 715, 850 660 C 1000 625, 1100 585, 1200 550" fill="none" stroke="var(--magenta)" stroke-width="9"/>
    <path d="M0 653 C 300 713, 600 728, 850 673 C 1000 638, 1100 598, 1200 563" fill="none" stroke="var(--magenta-dark)" stroke-width="3" opacity="0.7"/>
  </svg>

  <div class="frame"></div>

  <h1 class="title">LEAP PULSE STRIDE</h1>
  <p class="subtitle">Auditions</p>

  <svg class="date-ribbon" width="836" height="54" viewBox="0 0 836 54" aria-hidden="true">
    <polygon points="0,6 30,6 18,27 30,48 0,48" fill="var(--magenta-dark)"/>
    <polygon points="836,6 806,6 818,27 806,48 836,48" fill="var(--magenta-dark)"/>
    <rect x="14" y="2" width="808" height="50" fill="var(--magenta)"/>
  </svg>
  <p class="date-text">THURSDAY JUNE 30TH, 6:30-8:30 PM IN PERSON</p>

  <p class="address">4172 Kestrel BLVD, Oakland CA 94605</p>
  <p class="welcome">Teens and Adults Welcomed</p>

  <div class="dancer-art" role="img" aria-label="Illustration of a leaping dancer silhouette surrounded by yellow and purple floral swirls"></div>

  <ul class="details">
    <li>
      <svg class="marker" viewBox="0 0 26 26" aria-hidden="true"><circle cx="13" cy="13" r="12" fill="var(--magenta)"/></svg>
      Video submissions turn in by<strong>Sunday July 3rd, 2022</strong>
    </li>
    <li>
      <svg class="marker" viewBox="0 0 26 26" aria-hidden="true">
        <circle cx="13" cy="13" r="12" fill="var(--magenta)"/>
        <rect x="6.5" y="8.5" width="13" height="9" fill="none" stroke="var(--white)" stroke-width="1.6"/>
        <polyline points="6.5,8.5 13,14 19.5,8.5" fill="none" stroke="var(--white)" stroke-width="1.6"/>
      </svg>
      email:<strong>LeapPulseStride22@movenote.test</strong>
    </li>
  </ul>
</main>
</body>
</html>
```